Tarno Booking website (www.tarnobooking.example)

My company develops booking software, Tarno Booking, for the hourly booking of resources such as classes in a school or customer booking involving rooms in a spa. These bookings also involve the customers, staff, rooms and a lesson or treatment.

The main difference between this software and general calendar software such as Plexo calendar is that this Tarno Booking allows resources such as people and rooms to be associated with the bookings. This is important for example in the case of a Spa to make sure the rooms are booked appropriately and to see the free times for the rooms. For a golf practice range the players much be booked to the tee spots where they practice golf.

I have tried to design the website myself, as a computer programmer- I am a bit "square" and not a designer, my first attempt is http://www.tarnobooking.example/, my second attempt is at http://www.quenbel-works.example/tarnobookingwebsite/
I am not happy with my designs as compared to the professional designs I see people can come up with here. The software must have the image of a professional software product in order to inspire the confidence of customers.

Am looking for a design which will be the most likely to give the customer the following feeling:
* Confident the product can do the job.
* Feel easy to want to try it, at least for the free trial.
* Its a professional software product and also a web based product, the user can login from the web.

Look at other booking software websites for ideas, here is a list of links to similar booking products. These products all have different features but are mostly for resource booking.
http://quenbel-works.example/tarnobookingwebsite/?page=compare

Hello all,

Thankyou for the designs so far, to save peoples time, I will try to eliminate the bottom 50% of designs now.

To be honest, most of the designs are of a good or high quality, I think its very tough on you as graphic and web designers. Only a minor few are of low quality.

If your design is discarded - I would say its unlikely that you are going to be able to produce a design that will beat the competition. 
You probably already know, you could try to re-sell your design later for other projects or as a template on one of those template websites. Some of these discarded designs are quite worthwhile designs.

Best regards, Dorian

Target Market(s)

Spa, Gym, School, Golf, any organization who manages bookings of their customers

Industry/Entity Type

Software

Requirements
Must have
• Home page and inner page, any other pages up to you.

Make a logo or use the image of the girl that I already have on the second design.

Menu(s) for navigation.

A language switcher for 3 languages, English, Chinese Traditional and Chinese Simplified. (Western, Hong Kong and Chinese mainland market are important).

Space for a video introduction, it could be small and when the user clicks on it then it gets bigger then it won't take up too much space. Up to you.

A space for the user to login and register a new account.

Screenshots.

I don't have any strong preferences, use your own ideas, if you look at all the other products you can get the basic idea from them.

The total goal is to make a website which is going to lead to sales of the software product.

```html
<!DOCTYPE html>
<html lang="en">
<head>
<meta charset="utf-8">
<title>Tarno Booking – Bookings</title>
<link rel="stylesheet" href="https://fonts.googleapis.com/css2?family=Mulish:wght@400;600;700;800&family=Pinyon+Script&display=swap">
<style>
:root{
  --sky-edge:#7fc2d1;
  --sky-mid:#c6e6ee;
  --sky-core:#ffffff;
  --binder:#2b2b2b;
  --page:#ecedee;
  --page-light:#f3f4f5;
  --rule:#c9cccf;
  --ink:#4a4d50;
  --ink-soft:#8b8f93;
  --tab:#6eb2c2;
  --tab-dark:#5a9fb0;
  --footer:#6db0c0;
  --field-border:#c4d3d9;
  --white:#ffffff;
}
*{box-sizing:border-box;margin:0;padding:0}
html,body{width:1200px;height:900px;overflow:hidden}
body{
  position:relative;
  font-family:"Mulish",sans-serif;
  color:var(--ink);
  background:radial-gradient(ellipse 62% 58% at 50% 48%,var(--sky-core) 0%,var(--sky-core) 45%,var(--sky-mid) 78%,var(--sky-edge) 100%);
}
.abs{position:absolute}

/* language switcher */
.language{top:10px;left:918px;font-size:13px;color:#4d6a75;display:flex;align-items:center;gap:10px}
.language .opt{display:flex;align-items:center;gap:4px}
.radio{width:12px;height:12px;border-radius:50%;background:var(--white);border:1px solid #b9c4c8;display:inline-block;position:relative}
.radio.on::after{content:"";position:absolute;left:3px;top:3px;width:4px;height:4px;border-radius:50%;background:#555}

/* binder */
.binder{left:86px;top:96px;width:1019px;height:731px;background:var(--binder);border-radius:14px;box-shadow:0 4px 14px rgba(0,0,0,.35)}
.page-stack{left:1058px;top:124px;width:10px;height:674px;background:linear-gradient(90deg,#d8dadc,#bfc2c5);border-radius:0 6px 6px 0}
.page-left{left:105px;top:123px;width:290px;height:677px;background:linear-gradient(180deg,var(--page-light),var(--page));border-radius:3px 0 0 3px}
.page-right{left:408px;top:123px;width:653px;height:677px;background:linear-gradient(180deg,var(--page-light),var(--page));border-radius:0 3px 3px 0}
.rings{left:378px;top:170px}

/* tabs */
.tabs{left:408px;top:86px;display:flex;gap:6px;list-style:none;z-index:5}
.tab{height:37px;background:linear-gradient(180deg,#80bfcd,var(--tab-dark));color:var(--white);font-weight:800;font-size:15.5px;display:flex;align-items:center;justify-content:center;border-radius:3px 3px 0 0;white-space:nowrap}
.tab.active{background:linear-gradient(180deg,#f6f7f8,var(--page-light));color:#3f4245;height:40px;margin-top:-3px}

/* steps */
.steps{left:447px;top:145px;width:578px;height:47px;background:linear-gradient(180deg,#fbfbfc,#e9ebec);border:1px solid #d6d9db;box-shadow:0 1px 2px rgba(0,0,0,.12)}
.steps svg{position:absolute;left:0;top:0}
.step{position:absolute;top:0;height:45px;line-height:45px;font-size:13.5px;color:#a2a5a8}
.step.current{color:#3d4043;font-weight:700}

.rule{height:1px;background:var(--rule);box-shadow:0 1px 0 #fff}
.section-title{left:462px;top:237px;font-size:15px;font-weight:700;color:#55585b}

/* form */
.field-label{width:120px;text-align:right;font-size:15px;font-weight:700;color:#6a6e72}
.field{left:582px;width:363px;height:35px;background:var(--white);border:1px solid var(--field-border);border-radius:3px;font-size:14px;color:#9a9ea2;padding:0 11px;line-height:33px}
.field.select .arrow{position:absolute;right:0;top:0;width:42px;height:33px;border-left:1px solid var(--field-border);background:linear-gradient(180deg,#f4f6f7,#e2e6e8)}
.field.select svg{position:absolute;left:14px;top:13px}
.field.notes{height:140px;line-height:1.4;padding-top:7px}

.button{background:linear-gradient(180deg,#fbfbfb,#d9dbdd);border:1px solid #c2c5c8;border-radius:4px;box-shadow:0 1px 2px rgba(0,0,0,.18);color:#55585b;font-size:14.5px;text-align:center}
.next{left:920px;top:727px;width:90px;height:30px;line-height:28px}

/* left page */
.mascot{left:182px;top:33px;width:117px;height:234px;border-radius:40px 40px 6px 6px;background:linear-gradient(180deg,#a0522d 0%,#e9b98f 30%,#f3cfa8 45%,#ffffff 60%,#1e1e1e 72%,#e5b48a 90%,#1e1e1e 100%)}
.sign{left:129px;top:146px;width:223px;height:71px;background:var(--white);border:1px solid #cfd2d4;box-shadow:0 1px 3px rgba(0,0,0,.2);display:flex;align-items:center;justify-content:center;font-size:25px;font-weight:600;color:#3a3a3a}
.side-rule{left:131px;width:221px}
.client{left:131px;top:309px;width:221px;text-align:center;font-size:17px;font-weight:700;color:#3f4245}
.welcome{left:131px;top:360px;font-family:"Pinyon Script",cursive;font-size:33px;color:#6a6e72}
.info-label{left:143px;font-size:13px;font-weight:800;color:#55585b}
.info-value{left:143px;font-size:13.5px;color:#5c6064}
.signout{left:260px;top:540px;width:92px;height:31px;line-height:29px}
.news-head{left:135px;top:607px;font-size:15px;font-weight:800;color:#3f4245}
.news-title{left:136px;font-size:13.5px;color:#5c6064}
.news-date{left:136px;font-size:11.5px;color:#6f7377}

/* footer */
.footer{left:0;top:860px;width:1200px;height:40px;background:var(--footer)}
.footer-nav{left:104px;top:872px;display:flex;list-style:none;font-size:13.5px;font-weight:700;color:var(--white)}
.footer-nav li{margin-right:22px}
.copyright{left:975px;top:872px;font-size:13px;font-weight:800;color:#3f7585}
</style>
</head>
<body>

<div class="abs language">
  <span>Language:</span>
  <span class="opt"><span class="radio on"></span>English</span>
  <span class="opt"><span class="radio"></span>体体</span>
  <span class="opt"><span class="radio"></span>繁體</span>
</div>

<div class="abs binder"></div>
<div class="abs page-stack"></div>
<div class="abs page-left"></div>
<div class="abs page-right"></div>

<ul class="abs tabs">
  <li class="tab" style="width:91px">About</li>
  <li class="tab active" style="width:94px">Bookings</li>
  <li class="tab" style="width:86px">Free Trial</li>
  <li class="tab" style="width:137px">Documentation</li>
  <li class="tab" style="width:94px">Purchase</li>
  <li class="tab" style="width:94px">Compare</li>
</ul>

<svg class="abs rings" width="46" height="608" viewBox="0 0 46 608" aria-hidden="true">
  <defs>
    <g id="ring">
      <rect x="3" y="-4" width="40" height="8" rx="4" fill="#111" stroke="#d9d9d9" stroke-width="2.2"/>
    </g>
    <g id="ring-pair">
      <use href="#ring" y="0"/>
      <use href="#ring" y="16"/>
    </g>
  </defs>
  <use href="#ring-pair" y="12"/>
  <use href="#ring-pair" y="64"/>
  <use href="#ring-pair" y="117"/>
  <use href="#ring-pair" y="246"/>
  <use href="#ring-pair" y="299"/>
  <use href="#ring-pair" y="351"/>
  <use href="#ring-pair" y="474"/>
  <use href="#ring-pair" y="527"/>
  <use href="#ring-pair" y="580"/>
</svg>

<!-- left page -->
<div class="abs mascot" role="img" aria-label="Mascot illustration of a cheerful receptionist holding the brand sign"></div>
<div class="abs sign">Tarno Booking</div>

<div class="abs rule side-rule" style="top:291px"></div>
<div class="abs client">The Lumen Spa Group</div>
<div class="abs rule side-rule" style="top:348px"></div>
<div class="abs welcome">Welcome Back!</div>
<div class="abs rule side-rule" style="top:418px"></div>

<div class="abs info-label" style="top:434px">Website:</div>
<div class="abs info-value" style="top:450px">www.lumenspa.example</div>
<div class="abs info-label" style="top:484px">Email:</div>
<div class="abs info-value" style="top:500px">info@lumenspa.example</div>
<div class="abs info-label" style="top:531px">Phone:</div>
<div class="abs info-value" style="top:547px">+27 555 0192</div>
<div class="abs button signout">Sign Out</div>

<div class="abs rule side-rule" style="top:587px"></div>
<div class="abs news-head">Latest News</div>
<div class="abs news-title" style="top:638px">News title goes here</div>
<div class="abs news-date" style="top:657px">31 October 2011</div>
<div class="abs news-title" style="top:691px">News title goes here</div>
<div class="abs news-date" style="top:710px">29 October 2011</div>
<div class="abs news-title" style="top:744px">News title goes here</div>
<div class="abs news-date" style="top:763px">8 October, 2011</div>

<!-- right page -->
<div class="abs steps">
  <svg width="578" height="45" viewBox="0 0 578 45" aria-hidden="true">
    <g fill="none" stroke="#d3d6d8" stroke-width="1.2">
      <polyline points="133,0 155,22.5 133,45"/>
      <polyline points="276,0 298,22.5 276,45"/>
      <polyline points="418,0 440,22.5 418,45"/>
    </g>
  </svg>
  <span class="step current" style="left:30px">1. Details</span>
  <span class="step" style="left:163px">2. Date &amp; Time</span>
  <span class="step" style="left:316px">3. Schedule</span>
  <span class="step" style="left:467px">4. Confirm</span>
</div>

<div class="abs rule" style="left:462px;top:214px;width:551px"></div>
<div class="abs section-title">Customer Details</div>
<div class="abs rule" style="left:462px;top:274px;width:551px"></div>

<div class="abs field-label" style="left:443px;top:327px">Name:</div>
<div class="abs field" style="top:319px">Name</div>
<div class="abs field-label" style="left:443px;top:374px">Phone:</div>
<div class="abs field" style="top:366px">Phone</div>
<div class="abs field-label" style="left:443px;top:421px">Email:</div>
<div class="abs field" style="top:413px">Email Address</div>
<div class="abs field-label" style="left:443px;top:467px">Group:</div>
<div class="abs field select" style="top:459px">Amont of People Attending
  <span class="arrow"><svg width="14" height="9" viewBox="0 0 14 9" aria-hidden="true"><polygon points="0,0 14,0 7,9" fill="#6da6b6"/></svg></span>
</div>
<div class="abs field-label" style="left:443px;top:514px">Notes:</div>
<div class="abs field notes" style="top:506px">Special Requirements&nbsp; /&nbsp; Medical Conditions</div>

<div class="abs rule" style="left:462px;top:702px;width:551px"></div>
<div class="abs button next">next...</div>
<div class="abs rule" style="left:462px;top:776px;width:551px"></div>

<!-- footer -->
<div class="abs footer"></div>
<ul class="abs footer-nav">
  <li>About</li><li>Events</li><li>Press</li><li>Jobs</li><li>Staff</li><li>Resources</li><li>Privacy</li><li>T&amp;Cs</li><li>Feedback</li><li>Customer Service</li><li>Contact</li>
</ul>
<div class="abs copyright">© 2011 Tarno Booking</div>

</body>
</html>
```